logo and label design for a vegan skincare Called Leafmerelle

We need a logo and label design for a skincare brand called leafmerelle based in Australia. The products are 100% natural, Australian made, small batch, vegan, cruelty-free, ethical and sustainable beauty products. The secret of our skin care products are their naturally active ingredients.
They are potent, yet incredibly gentle on sensitive skin. We believe in investing in only the highest quality and ethical ingredients to ensure we are creating products we can stand behind.
Our products use: Naturally delivered ingredients; Organic ingredients where is possible; Australian oils, fruits & Extracts; Aromatherapy oils; sustainable & ethical ingredients; natural preservatives.
Our products don't use: sulphates; parabens; phthalates; Petrochemicals; synthetic colours; synthetic fragrances. All label must be design for an amber bottle.
Label Requirements:
* 300 DPI minimum
* All fonts have been outlined
* 3mm Bleed included in artwork
Colors
Designer to choose colors to be used in the design.
Look and feel
Each slider illustrates characteristics of the customer's brand and the style your logo design should communicate.

```html
<!DOCTYPE html>
<html lang="en">
<head>
<meta charset="utf-8">
<title>Leafmerelle – Logo and Label Range</title>
<link href="https://fonts.googleapis.com/css2?family=Oswald:wght@500;600&family=Mulish:wght@400;500&family=Dancing+Script:wght@600&display=swap" rel="stylesheet">
<style>
  :root{
    --backdrop:#ececec;
    --label-cream:#e8e1d4;
    --ink:#1c1a19;
    --ink-soft:#3a3634;
  }
  *{box-sizing:border-box;margin:0;padding:0}
  html,body{width:1200px;height:663px;overflow:hidden}
  body{background:linear-gradient(180deg,#f1f1f1 0%,var(--backdrop) 60%,#e2e2e2 100%);position:relative;font-family:'Mulish',sans-serif;color:var(--ink)}

  .brand-lockup{position:absolute;left:566px;top:22px;width:371px;text-align:center}
  .brand-lockup__mark{display:block;width:103px;height:98px;margin:0 auto 16px;background:var(--ink)}
  .brand-lockup__name{font-family:'Mulish',sans-serif;font-weight:500;font-size:46px;letter-spacing:2px;line-height:1;text-transform:uppercase;color:var(--ink)}

  .label{position:absolute;background:var(--label-cream);display:flex;flex-direction:column;align-items:center;justify-content:space-between;text-align:center;padding:0 0}
  .label__band{width:100%;height:.95em;border-top:.35em solid var(--ink);border-bottom:.12em solid var(--ink);background:var(--label-cream)}
  .label__band--bottom{border-top:.12em solid var(--ink);border-bottom:.35em solid var(--ink)}
  .label__body{flex:1;display:flex;flex-direction:column;align-items:center;justify-content:space-evenly;width:100%;padding:0 .8em}
  .label__mark{width:3.6em;height:3.4em;background:var(--ink);margin-top:-.1em}
  .label__brand{font-family:'Mulish',sans-serif;font-weight:500;font-size:1.55em;letter-spacing:.06em;text-transform:uppercase;color:var(--ink-soft)}
  .label__title{font-family:'Oswald',sans-serif;font-weight:600;font-size:2.15em;line-height:1.12;text-transform:uppercase;color:var(--ink)}
  .label__ingredients{font-family:'Dancing Script',cursive;font-weight:600;font-size:1.2em;color:var(--ink-soft);border-top:.08em solid var(--ink);border-bottom:.08em solid var(--ink);padding:.2em .4em;white-space:nowrap}
  .label__dots{font-size:.9em;letter-spacing:.15em;line-height:.6}
  .label__claim{font-family:'Oswald',sans-serif;font-weight:500;font-size:1.1em;letter-spacing:.06em;text-transform:uppercase}
  .label__badges{display:flex;align-items:center;gap:.9em}
  .badge{width:2.5em;height:2.5em;border-radius:50%;border:.18em solid var(--ink)}
  .badge--origin{width:2.7em;height:2.5em;border:none;border-radius:0;background:var(--ink);clip-path:polygon(50% 0,100% 100%,0 100%)}
  .label__volume{font-size:1.1em;color:var(--ink-soft)}

  .label--cleanser{left:91px;top:272px;width:216px;height:273px;font-size:10px}
  .label--mist{left:384px;top:359px;width:163px;height:214px;font-size:7.6px}
  .label--mask{left:615px;top:345px;width:280px;height:242px;font-size:9.2px}
  .label--eye{left:971px;top:368px;width:147px;height:198px;font-size:6.9px}
  .label--mask .label__title{font-size:2.05em}
</style>
</head>
<body>

<header class="brand-lockup">
  <span class="brand-lockup__mark"></span>
  <h1 class="brand-lockup__name">Leafmerelle</h1>
</header>

<section class="label label--cleanser">
  <div class="label__band"></div>
  <div class="label__body">
    <span class="label__mark"></span>
    <p class="label__brand">Leafmerelle</p>
    <h2 class="label__title">Purifying<br>Gel Cleanser</h2>
    <p class="label__ingredients">· Lemon Tea Tree &amp; Vitamin E ·</p>
    <p class="label__dots">···</p>
    <p class="label__claim">Natural</p>
    <div class="label__badges"><span class="badge"></span><span class="badge"></span><span class="badge"></span><span class="badge badge--origin"></span></div>
    <p class="label__dots">···</p>
    <p class="label__volume">200 ml</p>
  </div>
  <div class="label__band label__band--bottom"></div>
</section>

<section class="label label--mist">
  <div class="label__band"></div>
  <div class="label__body">
    <span class="label__mark"></span>
    <p class="label__brand">Leafmerelle</p>
    <h2 class="label__title">Natural<br>AHA Toning Mist</h2>
    <p class="label__ingredients">· Quandong · Papaya · Lemongrass ·</p>
    <p class="label__dots">···</p>
    <div class="label__badges"><span class="badge"></span><span class="badge"></span><span class="badge"></span><span class="badge badge--origin"></span></div>
    <p class="label__dots">···</p>
    <p class="label__volume">100 ml</p>
  </div>
  <div class="label__band label__band--bottom"></div>
</section>

<section class="label label--mask">
  <div class="label__band"></div>
  <div class="label__body">
    <span class="label__mark"></span>
    <p class="label__brand">Leafmerelle</p>
    <h2 class="label__title">Pink Clay Calming Mask</h2>
    <p class="label__ingredients">· Calendula · Chamomile · Aloe Vera ·</p>
    <p class="label__dots">···</p>
    <p class="label__claim">Natural</p>
    <div class="label__badges"><span class="badge"></span><span class="badge"></span><span class="badge"></span><span class="badge badge--origin"></span></div>
    <p class="label__dots">···</p>
    <p class="label__volume">90 gr</p>
  </div>
  <div class="label__band label__band--bottom"></div>
</section>

<section class="label label--eye">
  <div class="label__band"></div>
  <div class="label__body">
    <span class="label__mark"></span>
    <p class="label__brand">Leafmerelle</p>
    <h2 class="label__title">Intensive Eye Cream</h2>
    <p class="label__ingredients">· Resveratrol · Shea Butter · Cucumber ·</p>
    <p class="label__dots">···</p>
    <p class="label__claim">Natural</p>
    <div class="label__badges"><span class="badge"></span><span class="badge"></span><span class="badge"></span><span class="badge badge--origin"></span></div>
    <p class="label__dots">···</p>
    <p class="label__volume">30 ml</p>
  </div>
  <div class="label__band label__band--bottom"></div>
</section>

</body>
</html>
```